Acoustic Album Needs Cover Design

Bence Morvath - Intentions: Quiet Harbor

The cover has five parts, each one has obligatory features:

The design in general could be that the person on the pictures is in white, empty space. Solve the shadows as you like, or use no shadows. Up to you.
The album is a happy, minimalistic, zen-like, acoustic album.

I. Main cover

Title: Intentions: Quiet Harbor
Artist: Bence Morvath
Image “01 main cover”

II. Cover inside

Track list (12 songs) with durations
All songs written by Bence Morvath
Copyright Bencetunes 2016.
Image “02 cover inside”

III. Disc

Artist: Bence Morvath
All songs written by Bence Morvath (round on the edge)
Copyright Bencetunes 2016. (round on the edge)
www.bencetunes-example.net (round on the edge)

IV. Under the disc

No words, only some design feature. (Not one of the three images!)

V. Cover back

Track list (same as cover inside)
Copyright Bencetunes 2016.
www.bencetunes-example.net
Image “05 backside”
The paper of this page is longer than the main cover, because it is to be turned up when put in the CD case, and there is the spine with the name of the Artist and Title of the album. On both ends.

Important:
The main cover I need in RGB and also CMYK, all the others only CMYK.
I need the work file (cdr, ai or whatever you use)
I need the CMYK images prepared for printing (sizes set, and that little extra on the edges).
I need the RGB main cover cover in jpeg, 3000x3000 pixels.
That's all. :)

The most important of these all is of course the main cover RGB. Make this one first!

Here’s a sample to listen, it might inspire you:
https://files.filevault-example.net/u/83610457/Quiet%20Harbor%20medley%2020160118.mp3

If you take a closer look at my website, you can see the whole concept.

Good luck and enjoy!
Regards,
Bence

Target Market(s)

New Age spiritual people.

Requirements
Must have
• The three images:
• https://www.filevault-example.net/s/kqpwmrtz7hba2ne/01%20main%20cover%2020160221.jpg?dl=0
• https://www.filevault-example.net/s/9hlyt3wfq5mn8re/02%20cover%20inside%2020160221.jpg?dl=0
• https://www.filevault-example.net/s/pnr4gdk2vjs7bto/05%20backside%2020160221.jpg?dl=0
• If there's a technical problem, let me know!

```html
<!DOCTYPE html>
<html lang="en">
<head>
<meta charset="utf-8">
<title>Intentions: Quiet Harbor — Bence Morvath</title>
<link rel="stylesheet" href="https://fonts.googleapis.com/css2?family=Josefin+Sans:wght@300;400;600&family=Open+Sans:wght@400;600&display=swap">
<style>
  :root {
    --bg: #ececec;
    --paper: #ffffff;
    --orange: #f5a81c;
    --ink: #222222;
    --soft-ink: #444444;
    --line: #d4d4d4;
    --shirt: #a9c8ea;
    --khaki: #c7b79a;
    --wood: #d9b27a;
  }
  * { box-sizing: border-box; margin: 0; padding: 0; }
  html, body { width: 1200px; height: 1200px; overflow: hidden; background: var(--bg); }
  .canvas { position: relative; width: 1200px; height: 1200px; }
  .panel {
    position: absolute; background: var(--paper);
    box-shadow: 0 2px 10px rgba(0,0,0,0.12);
    font-family: "Open Sans", Arial, sans-serif; color: var(--ink);
  }
  .photo {
    position: absolute; border-radius: 40px;
    background: radial-gradient(ellipse at 50% 40%, var(--shirt) 0%, #c9d9ea 35%, var(--khaki) 70%, rgba(255,255,255,0) 100%);
  }
  .photo.standing {
    border-radius: 60px;
    background: linear-gradient(180deg, #f2e2d6 0%, var(--shirt) 22%, var(--shirt) 48%, var(--khaki) 58%, var(--khaki) 90%, #fff 100%);
  }
  .album-title { font-family: "Josefin Sans", Arial, sans-serif; font-weight: 300; color: var(--orange); white-space: nowrap; }
  .album-title .lead { font-variant: small-caps; font-weight: 600; letter-spacing: 1.5px; }
  .tracklist { position: absolute; list-style: none; font-size: 8.5px; }
  .tracklist li { display: grid; grid-template-columns: 18px 1fr auto; align-items: center; }
  .tracklist .no { text-align: right; padding-right: 7px; }
  .credits { position: absolute; font-size: 8.5px; text-align: right; line-height: 1.6; white-space: nowrap; }

  /* main cover */
  .front { left: 144px; top: 172px; width: 404px; height: 392px; }
  .front .photo { left: 110px; top: 45px; width: 240px; height: 265px; }
  .front .album-title { position: absolute; left: 0; right: 0; top: 318px; text-align: center; font-size: 24px; }
  .front .artist-band {
    position: absolute; left: 0; right: 0; top: 347px; height: 21px; background: var(--orange);
    color: #fff; text-align: center; font-family: "Josefin Sans", Arial, sans-serif; font-weight: 300;
    font-size: 16px; line-height: 23px; letter-spacing: 0.5px;
  }

  /* back cover */
  .back { left: 640px; top: 172px; width: 452px; height: 392px; }
  .back .tracklist { left: 102px; top: 62px; width: 140px; }
  .back .tracklist li { height: 18.8px; }
  .back .album-title { position: absolute; right: 210px; top: 290px; font-size: 18px; }
  .back .credits { right: 210px; top: 313px; }
  .back .web { position: absolute; right: 210px; top: 358px; font-size: 11px; letter-spacing: 0.4px; }
  .back .photo { left: 270px; top: 32px; width: 150px; height: 345px; }

  /* inside cover */
  .inside { left: 32px; top: 620px; width: 414px; height: 404px; }
  .inside .album-title { position: absolute; font-size: 23px; }
  .inside .title-lead { left: 66px; top: 58px; }
  .inside .title-main { left: 86px; top: 84px; }
  .inside .tracklist { left: 84px; top: 122px; width: 130px; }
  .inside .tracklist li { height: 16.6px; }
  .inside .credits { right: 200px; top: 336px; }
  .inside .photo { left: 244px; top: 22px; width: 150px; height: 350px; }

  /* disc */
  .disc { position: absolute; left: 788px; top: 694px; width: 400px; height: 400px; }
</style>
</head>
<body>
<main class="canvas">

  <section class="panel front" aria-label="Main cover">
    <div class="photo" role="img" aria-label="Photo of the artist seated cross-legged in a blue shirt playing an acoustic guitar, a small yellow flower beside him"></div>
    <h1 class="album-title"><span class="lead">Intentions:</span> Quiet Harbor</h1>
    <div class="artist-band">Bence Morvath</div>
  </section>

  <section class="panel back" aria-label="Back cover">
    <ol class="tracklist">
      <li><span class="no">1</span><span>Piano Relax</span><span>5:30</span></li>
      <li><span class="no">2</span><span>Relax dummy copy</span><span>4:15</span></li>
      <li><span class="no">3</span><span>Relax dummy</span><span>6:10</span></li>
      <li><span class="no">4</span><span>Dummy Relax</span><span>3:45</span></li>
      <li><span class="no">5</span><span>Piano Relax</span><span>7:15</span></li>
      <li><span class="no">6</span><span>Relax dummy copy</span><span>5:30</span></li>
      <li><span class="no">7</span><span>Relax dummy</span><span>4:15</span></li>
      <li><span class="no">8</span><span>Dummy Relax</span><span>6:10</span></li>
      <li><span class="no">9</span><span>Piano Relax</span><span>3:45</span></li>
      <li><span class="no">10</span><span>Relax dummy copy</span><span>7:15</span></li>
      <li><span class="no">11</span><span>Relax dummy</span><span>7:15</span></li>
      <li><span class="no">12</span><span>Dummy Relax</span><span>5:30</span></li>
    </ol>
    <h2 class="album-title"><span class="lead">Intentions:</span> Quiet Harbor</h2>
    <p class="credits">All songs written by Bence Morvath<br>Copyright Bencetunes 2016</p>
    <p class="web">www.bencetunes-example.net</p>
    <div class="photo standing" role="img" aria-label="Photo of the artist standing barefoot holding a guitar by the neck, with a yellow flower in soil"></div>
  </section>

  <section class="panel inside" aria-label="Inside cover">
    <h2 class="album-title title-lead"><span class="lead">Intentions:</span></h2>
    <h2 class="album-title title-main">Quiet Harbor</h2>
    <ol class="tracklist">
      <li><span class="no">1</span><span>Piano Relax</span><span>5:30</span></li>
      <li><span class="no">2</span><span>Relax dummy copy</span><span>4:15</span></li>
      <li><span class="no">3</span><span>Relax dummy</span><span>6:10</span></li>
      <li><span class="no">4</span><span>Dummy Relax</span><span>3:45</span></li>
      <li><span class="no">5</span><span>Piano Relax</span><span>7:15</span></li>
      <li><span class="no">6</span><span>Relax dummy copy</span><span>5:30</span></li>
      <li><span class="no">7</span><span>Relax dummy</span><span>4:15</span></li>
      <li><span class="no">8</span><span>Dummy Relax</span><span>6:10</span></li>
      <li><span class="no">9</span><span>Piano Relax</span><span>3:45</span></li>
      <li><span class="no">10</span><span>Relax dummy copy</span><span>7:15</span></li>
      <li><span class="no">11</span><span>Relax dummy</span><span>7:15</span></li>
      <li><span class="no">12</span><span>Dummy Relax</span><span>5:30</span></li>
    </ol>
    <p class="credits">All songs written by Bence Morvath<br>Copyright Bencetunes 2016</p>
    <div class="photo standing" role="img" aria-label="Photo of the artist standing with a guitar resting on the floor beside him and a yellow flower in soil"></div>
  </section>

  <svg class="disc" viewBox="0 0 400 400" aria-label="Disc label">
    <defs>
      <clipPath id="disc-clip"><circle cx="200" cy="200" r="199"/></clipPath>
      <linearGradient id="guitar-tone" x1="0" y1="0" x2="1" y2="1">
        <stop offset="0" stop-color="#e9d2a4"/>
        <stop offset="0.6" stop-color="#d9b27a"/>
        <stop offset="1" stop-color="#9a5a32"/>
      </linearGradient>
      <path id="rim-path" d="M 30 270 A 182 182 0 0 0 370 270"/>
    </defs>
    <circle cx="200" cy="200" r="199" fill="#fff" stroke="#cfcfcf" stroke-width="1.2"/>
    <g clip-path="url(#disc-clip)">
      <rect x="318" y="60" width="90" height="240" rx="38" fill="url(#guitar-tone)" role="img" aria-label="Detail of an acoustic guitar with a yellow flower sprouting from soil"/>
      <ellipse cx="315" cy="225" rx="38" ry="40" fill="#f3d977" opacity="0.55"/>
    </g>
    <circle cx="200" cy="200" r="62" fill="none" stroke="#9a9a9a" stroke-width="1"/>
    <circle cx="200" cy="200" r="54" fill="none" stroke="#c4c4c4" stroke-width="1"/>
    <circle cx="200" cy="200" r="46" fill="#f4f4f4" stroke="#d8d8d8" stroke-width="1"/>
    <text x="200" y="46" text-anchor="middle" font-family="'Josefin Sans', Arial, sans-serif" font-weight="300" font-size="15" fill="#444">Bence Morvath</text>
    <text x="270" y="298" text-anchor="end" font-family="'Josefin Sans', Arial, sans-serif" font-weight="600" font-size="17" fill="#f5a81c" letter-spacing="1.5" style="font-variant: small-caps">Intentions:</text>
    <text x="270" y="325" text-anchor="end" font-family="'Josefin Sans', Arial, sans-serif" font-weight="300" font-size="23" fill="#f5a81c">Quiet Harbor</text>
    <text font-family="'Open Sans', Arial, sans-serif" font-size="8.5" fill="#222">
      <textPath href="#rim-path" startOffset="50%" text-anchor="middle">All songs written by Bence Morvath  -  Copyright Bencetunes 2016  -  www.bencetunes-example.net</textPath>
    </text>
  </svg>

</main>
</body>
</html>
```